Business card design for global fintech startup

Veltrix is a modern payments platform for the global insurance industry, serving international health, life, and travel insurers, MGAs, brokers, and partners.

We need a professional, premium business card for use at insurance conferences and executive meetings. The goal is to create a card that feels trustworthy, modern, and high-quality, while still being distinctive and memorable in a stack of business cards.

Target audience:
Senior insurance executives (VP, C-suite).

Design goals:
Clear, professional, and credible
Modern but not trendy
Premium and well-structured
Easy to read and practical for networking

Brand direction:
Brand-first (company over individual)
Follow existing brand guidelines where possible
Clean layout, strong hierarchy, excellent readability

Must include:
Name
Title
Company name (Veltrix)
Logo
Email
Phone/Whatsapp
Website (www.withveltrix.example)
Tagline - Secure flows, anywhere

Materials & finish:
Open to designer recommendations for premium look and feel.

Please avoid:
Flashy or trendy startup styles
Generic insurance icons or clichés
Cluttered layouts or hard-to-read text

Deliverables:
Front and back business card, print-ready files.

Target Market(s)

Global Insurance executives

Industry/Entity Type

Fintech, Insurtech, Insurance, Financial Services

Contact Information for Business Card

Name Title Company name (Veltrix) Logo Email Phone/Whatsapp Website (www.withveltrix.example) Tagline - Secure flows, anywhere

Font styles to use
Other font styles liked:
• See brand guidelines

Requirements
Nice to have
• something that stands out/makes us more memorable while still remaining professional
Should not have
• Please avoid: Flashy or trendy startup styles Generic insurance icons or clichés Cluttered layouts or hard-to-read text

```html
<!DOCTYPE html>
<html lang="en">
<head>
<meta charset="utf-8">
<title>Veltrix business card – front and back</title>
<link rel="stylesheet" href="https://fonts.googleapis.com/css2?family=Montserrat:wght@400;500;600;700&display=swap">
<style>
  :root {
    --bg: #ababab;
    --paper: #ffffff;
    --ink: #222222;
    --ink-soft: #3a3a3a;
    --orange: #f47a20;
    --yellow: #f8c35c;
    --purple: #5b3f98;
    --blue: #3b82c9;
    --sky: #3ec3ea;
    --dark: #232323;
  }
  * { box-sizing: border-box; margin: 0; padding: 0; }
  html, body { width: 1081px; height: 1200px; overflow: hidden; }
  body {
    background: var(--bg);
    font-family: "Montserrat", sans-serif;
    display: flex;
    flex-direction: column;
    align-items: center;
    justify-content: center;
    gap: 60px;
  }
  .card {
    position: relative;
    width: 900px;
    height: 513px;
    border-radius: 40px;
    overflow: hidden;
  }
  /* Front */
  .card--front { background: var(--paper); }
  .brand {
    position: absolute;
    left: 48px;
    top: 72px;
    display: flex;
    align-items: center;
    gap: 18px;
  }
  .brand__dot {
    width: 40px; height: 40px; border-radius: 50%;
    background: var(--orange);
  }
  .brand__name {
    font-weight: 600;
    font-size: 56px;
    letter-spacing: 5px;
    text-transform: uppercase;
    color: var(--ink);
    line-height: 1;
  }
  .person {
    position: absolute;
    right: 50px;
    top: 72px;
    text-align: right;
  }
  .person__name {
    font-weight: 700;
    font-size: 35px;
    letter-spacing: 1px;
    text-transform: uppercase;
    line-height: 1;
  }
  .person__first { color: var(--orange); }
  .person__last { color: var(--sky); }
  .person__title {
    font-size: 22px;
    color: var(--ink-soft);
    margin-top: 2px;
  }
  .accent-block {
    position: absolute;
    right: 0; top: 76px;
    width: 23px; height: 51px;
    background: var(--sky);
  }
  .contact {
    position: absolute;
    left: 48px;
    top: 338px;
    list-style: none;
  }
  .contact li {
    display: flex;
    align-items: center;
    gap: 8px;
    font-size: 23px;
    color: var(--ink-soft);
    height: 35px;
  }
  .contact svg { width: 17px; height: 17px; flex: none; }
  .stripe {
    position: absolute;
    left: 0; right: 0; bottom: 0;
    height: 14px;
    display: flex;
  }
  .stripe span { flex: 1; }
  .stripe span:nth-child(1) { background: var(--yellow); }
  .stripe span:nth-child(2) { background: var(--orange); }
  .stripe span:nth-child(3) { background: var(--purple); }
  .stripe span:nth-child(4) { background: var(--blue); }
  .stripe span:nth-child(5) { background: var(--sky); }
  /* Back */
  .card--back { background: var(--dark); }
  .pattern {
    position: absolute; inset: 0;
    background: linear-gradient(100deg, #1c1c1c 0%, #262626 45%, #3a3a3a 80%, #4a4a4a 100%);
  }
  .brand--back {
    left: 50%; top: 50%;
    transform: translate(-50%, -62%);
  }
  .brand--back .brand__name { color: #ffffff; font-size: 60px; }
  .tagline {
    position: absolute;
    left: 50%; bottom: 0;
    transform: translateX(-50%);
    width: 440px; height: 50px;
    background: var(--orange);
    border-radius: 22px 22px 0 0;
    color: #ffffff;
    font-size: 25px;
    font-weight: 500;
    letter-spacing: 3px;
    display: flex; align-items: center; justify-content: center;
  }
</style>
</head>
<body>
  <section class="card card--front">
    <div class="brand">
      <span class="brand__dot"></span>
      <span class="brand__name">Veltrix</span>
    </div>
    <div class="person">
      <p class="person__name"><span class="person__first">Daniel</span> <span class="person__last">Reyes</span></p>
      <p class="person__title">Founder</p>
    </div>
    <span class="accent-block"></span>
    <ul class="contact">
      <li><svg viewBox="0 0 16 16"><path fill="#f47a20" d="M1 6c0-2 3-3.5 7-3.5S15 4 15 6v1.5h-3.5V6h-7v1.5H1zM3 9h10l1 5H2z"/></svg>(555) 010-2468</li>
      <li><svg viewBox="0 0 16 16"><circle cx="8" cy="8" r="6.3" fill="none" stroke="#f8c35c" stroke-width="1.6"/><path fill="#f8c35c" d="M5.5 5.3c.5-.5 1-.3 1.3.3l.4.9c.1.3 0 .6-.3.8.5 1 1.2 1.7 2.1 2.1.2-.3.5-.4.8-.3l.9.4c.6.3.8.8.3 1.3-1.8 1.5-6.5-2.9-5.5-5.5z"/></svg>(555) 010-2468</li>
      <li><svg viewBox="0 0 16 16"><rect x="1" y="3" width="14" height="10" fill="#3b82c9"/><path d="M1 3l7 6 7-6" fill="none" stroke="#fff" stroke-width="1.3"/></svg>info@withveltrix.example</li>
      <li><svg viewBox="0 0 16 16"><circle cx="8" cy="8" r="7" fill="#3ec3ea"/><path d="M1 8h14M8 1c3 3 3 11 0 14M8 1c-3 3-3 11 0 14" fill="none" stroke="#fff" stroke-width="1"/></svg>www.withveltrix.example</li>
    </ul>
    <div class="stripe"><span></span><span></span><span></span><span></span><span></span></div>
  </section>

  <section class="card card--back">
    <div class="pattern" role="img" aria-label="Embossed dark repeating pattern texture"></div>
    <div class="brand brand--back">
      <span class="brand__dot"></span>
      <span class="brand__name">Veltrix</span>
    </div>
    <p class="tagline">Secure flows, anywhere</p>
  </section>
</body>
</html>
```